Business Card and Letterhead Design for Public Accounting Firm

Business card and letterhead design for a CPA Firm located in Orange County, CA. We're looking for a modern and professional design utilizing our existing logo. We'd like a clean "less is more" look, but also something that catches the eye. We provide a high level of service to our clients. Open to single or double sided business cards.

Additional info: color numbers on logo
Blue :
R 0
G 83
B 125

#00537D

Silver :

R 154
G 154
B 154

#9A9A9A

Target Market(s)

Businesses and individuals

Industry/Entity Type

Accounting

Contact Information for Business Card

Moss Whitfield & Danby LLP - 4827 Larkspur Vale Road, Irvine, CA 92614 - (949)731-2864 - mwdaccts.example

Font styles to use
Serif
Sans Serif
Other font styles liked:
• See font file uploaded

Colors
0054AA
0677BA
7BADD7
CADEEF
E8F1F8

Requirements
Nice to have
• Possibly use the font file provided which matches our logo, but adjust to be not in all caps

```html
<!DOCTYPE html>
<html lang="en">
<head>
<meta charset="utf-8">
<title>Moss Whitfield &amp; Danby LLP — Business Card</title>
<link rel="stylesheet" href="https://fonts.googleapis.com/css2?family=Tinos:wght@400;700&display=swap">
<style>
  :root {
    --brand-blue: #00537D;
    --brand-silver: #9A9A9A;
    --ink: #3a3a3a;
    --card: #ffffff;
    --backdrop: #8e8e8e;
  }
  * { margin: 0; padding: 0; box-sizing: border-box; }
  html, body { width: 1200px; height: 1200px; overflow: hidden; }
  body { background: var(--backdrop); font-family: "Tinos", "Times New Roman", serif; position: relative; }

  .card {
    position: absolute; left: 281px; width: 642px; height: 366px;
    background: var(--card); border-radius: 26px; overflow: hidden;
  }
  .card--front { top: 195px; }
  .card--back { top: 639px; }

  .person { position: absolute; right: calc(642px - 301px); top: 140px; text-align: right; }
  .person__name { color: var(--brand-blue); font-weight: 700; font-size: 22px; line-height: 1; white-space: nowrap; }
  .person__title { color: var(--brand-silver); font-size: 13px; margin-top: 6px; }

  .divider { position: absolute; width: 1px; background: var(--brand-silver); }
  .card--front .divider { left: 321px; top: 114px; height: 101px; }

  .contact { position: absolute; left: 341px; top: 110px; color: var(--ink); font-size: 14.5px; line-height: 21px; }
  .contact__firm { color: var(--brand-blue); font-weight: 700; }
  .contact__lines { margin-top: 0; }
  .contact__row { display: flex; align-items: center; gap: 6px; }
  .contact__row--first { margin-top: 5px; }
  .contact__icon { width: 11px; height: 11px; fill: var(--brand-blue); }

  .band { position: absolute; left: 0; right: 0; top: 310px; height: 26px; background: var(--brand-silver); }
  .band__blue {
    position: absolute; left: 0; top: 0; bottom: 0; width: 586px; background: var(--brand-blue);
    display: flex; align-items: center;
  }
  .band__url { position: absolute; left: 319px; transform: translateX(-50%); color: #fff; font-size: 13.5px; letter-spacing: 2.6px; white-space: nowrap; }
  .band__firm { position: absolute; right: 6px; color: #fff; font-size: 10px; white-space: nowrap; }

  .mark { position: absolute; left: 162px; top: 156px; width: 52px; height: 52px; border-radius: 50%; background: var(--brand-blue); }
  .card--back .divider { left: 290px; top: 138px; height: 89px; }
  .wordmark {
    position: absolute; left: 304px; top: 150px; color: var(--brand-silver);
    font-size: 29px; line-height: 31px; letter-spacing: 2.4px; text-transform: uppercase; white-space: nowrap;
  }
</style>
</head>
<body>
  <section class="card card--front">
    <div class="person">
      <div class="person__name">DANIEL HARPER</div>
      <div class="person__title">Founder &amp; CEO</div>
    </div>
    <div class="divider"></div>
    <div class="contact">
      <div class="contact__firm">Moss Whitfield &amp; Danby LLP</div>
      <div>4827 Larkspur Vale Road</div>
      <div>Irvine, CA 92614</div>
      <div class="contact__row contact__row--first">
        <svg class="contact__icon" viewBox="0 0 24 24" aria-hidden="true"><path d="M6.6 10.8a15 15 0 0 0 6.6 6.6l2.2-2.2a1 1 0 0 1 1-.25 11.4 11.4 0 0 0 3.6.57 1 1 0 0 1 1 1V20a1 1 0 0 1-1 1A17 17 0 0 1 3 4a1 1 0 0 1 1-1h3.5a1 1 0 0 1 1 1c0 1.25.2 2.45.57 3.57a1 1 0 0 1-.25 1z"/></svg>
        <span>(949)731-2864</span>
      </div>
      <div class="contact__row">
        <svg class="contact__icon" viewBox="0 0 24 24" aria-hidden="true"><path d="M2 5h20v14H2z M4 7v.5l8 5 8-5V7z" fill-rule="evenodd"/></svg>
        <span>cpas@mwdaccts.example</span>
      </div>
    </div>
    <div class="band">
      <div class="band__blue">
        <span class="band__url">www.mwdaccts.example</span>
        <span class="band__firm">Moss Whitfield &amp; Danby</span>
      </div>
    </div>
  </section>

  <section class="card card--back">
    <div class="mark" aria-hidden="true"></div>
    <div class="divider"></div>
    <div class="wordmark">Moss Whitfield<br>&amp; Danby LLP</div>
  </section>
</body>
</html>
```